Business Card Design

We are looking for a business card designed for our landscaping company. We do landscaping installation & Maintenance Services. We would like to see designs that have basic landscaping in background. We also think it is important to have both of our names and phone numbers on the card. We need something that stands out a little whether it is shape of the card or thickness or design.

Industry/Entity Type

Business

Contact Information for Business Card

Pale Ridge Yardworks, paleridgeyardworks@mailbrook.net, Dale Purvine 555-213-7690, Martin Kolbey 555-864-1037

```html
<!DOCTYPE html>
<html lang="en">
<head>
<meta charset="utf-8">
<title>Pale Ridge Yardworks – Business Card</title>
<link href="https://fonts.googleapis.com/css2?family=Source+Sans+3:wght@400;600;700&display=swap" rel="stylesheet">
<style>
  :root {
    --backdrop: #2a2a2a;
    --card: #ffffff;
    --green-dark: #3f7a3d;
    --green-light: #7cb342;
    --grass-top: #5f9a4f;
    --grass-base: #427a3e;
  }
  html, body {
    margin: 0;
    width: 1200px;
    height: 970px;
    overflow: hidden;
    background: var(--backdrop);
    font-family: "Source Sans 3", "Myriad Pro", sans-serif;
  }
  .business-card {
    position: absolute;
    left: 140px;
    top: 215px;
    width: 920px;
    height: 540px;
    background: var(--card);
    border-radius: 20px;
    overflow: hidden;
  }
  .brand-name {
    position: absolute;
    left: 110px;
    top: 150px;
    margin: 0;
    font-weight: 600;
    font-size: 50px;
    line-height: 1.05;
    color: var(--green-dark);
  }
  .contacts {
    position: absolute;
    left: 478px;
    top: 72px;
  }
  .person { margin: 0 0 22px; }
  .person-name {
    margin: 0;
    font-weight: 600;
    font-size: 46px;
    line-height: 1.05;
    color: var(--green-dark);
  }
  .person-phone {
    margin: 2px 0 0;
    font-size: 25px;
    color: var(--green-light);
  }
  .person-phone.strong { font-weight: 600; }
  .email {
    margin: 30px 0 0;
    font-size: 24px;
    color: var(--green-dark);
  }
  .email strong { font-weight: 700; }
  .email span { font-weight: 400; }
  .services {
    list-style: none;
    margin: 22px 0 0;
    padding: 0;
    font-weight: 600;
    font-size: 20px;
    line-height: 28px;
    color: var(--green-dark);
  }
  .services li::before {
    content: "•";
    color: var(--green-light);
    margin-right: 7px;
  }
  .grass-band {
    position: absolute;
    left: 0;
    bottom: 0;
    width: 920px;
    height: 165px;
  }
</style>
</head>
<body>
  <div class="business-card">
    <p class="brand-name">Pale Ridge<br>Yardworks</p>

    <div class="contacts">
      <div class="person">
        <p class="person-name">Dale Purvine</p>
        <p class="person-phone">555-213-7690</p>
      </div>
      <div class="person">
        <p class="person-name">Martin Kolbey</p>
        <p class="person-phone strong">555-864-1037</p>
      </div>
      <p class="email"><strong>paleridgeyardworks</strong><span>@mailbrook.net</span></p>
      <ul class="services">
        <li>Landscaping Installation</li>
        <li>Maintenance Services</li>
      </ul>
    </div>

    <svg class="grass-band" viewBox="0 0 920 165" role="img" aria-label="Illustration of a row of tall green grass blades along the bottom of the card">
      <defs>
        <linearGradient id="grassFade" x1="0" y1="0" x2="0" y2="1">
          <stop offset="0" stop-color="#ffffff" stop-opacity="0"/>
          <stop offset="0.35" stop-color="var(--grass-top)" stop-opacity="0.7"/>
          <stop offset="0.65" stop-color="var(--grass-base)"/>
          <stop offset="1" stop-color="var(--grass-base)"/>
        </linearGradient>
      </defs>
      <rect x="0" y="0" width="920" height="165" fill="url(#grassFade)"/>
    </svg>
  </div>
</body>
</html>
```